Real Estate Flyer (Brenton Property)

We need a color CMYK high resolution, print quality horizontal real estate property flyer designed in the sizes of 10" wide and 6.7425" tall and another one in 11" wide and 8.5" tall.
Ad should be professionally looking to U.S. standards. It should be sleek, modern yet classy.
We uploaded in Briefs logo files, agent photo, 2 photos of the property (Must use both) and a sample of a flyer for Vayle Morrow Luxury Residence. We like how the overlay atop the first photo in the Vayle Morrow flyer with the company logo in the overlay. We'd like to incorporate that with our logo, the background color of the overlay should match that of our logo. DON'T CHANGE LOGO COLORS. Only use two colors in ad (exact logo blue color and white). The text in the overlay must be "FOR SALE - Potential Income Producing Commercial Office Building". Other details that should be prominent underneath are "42 Brenton Dr., Schaumburg, IL 60174 - Asking Price: $650,000".
Add "Residential & Commercial" under our company logo in italic font.
Add in flyer: "Located seconds away from the Kettering Rd. & Palden Rd. Intersection"
Add in flyer:
- Completely vacant
- 10,000 sq. ft. building
- 55 Car Parking
- 1.38 acre lot
- Over 20 offices and 5 bathrooms.
- Lease out individual office spaces for great monthly cash flow
Put agent's photo and following details professionally displayed:
Dev Marlo
Managing Broker
847-555-0148
dev.marlo@qtnhomes-example.com
Add from Briefs fair housing logo and PLX logo near agent's information. Logos should be small but yet visible to understand text.
Add at bottom of the ad with separation near agent details:
Looking to Buy or Sell?
I’m your one-stop, full service licensed real estate broker.
I deal with all types of real estate properties: Homes, Condos, Townhomes, Multi-Unit Apartment Buildings and Commercial Spaces.
Let My Experience Guide You Through Every Step of the Process!
Fine print:
©2018 QTN Homes, Inc. All Rights Reserved.

```html
<!DOCTYPE html>
<html lang="en">
<head>
<meta charset="utf-8">
<title>Brenton Property – For Sale</title>
<link href="https://fonts.googleapis.com/css2?family=Open+Sans:ital,wght@0,300;0,400;0,500;0,600;1,400&family=Crimson+Text:wght@400&display=swap" rel="stylesheet">
<style>
  :root{
    --brand-blue:#0a3cf5;
    --ink-blue:#12287e;
    --white:#ffffff;
    --ink:#1a1a1a;
  }
  *{margin:0;padding:0;box-sizing:border-box}
  html,body{width:1200px;height:800px;overflow:hidden;background:var(--white)}
  body{font-family:"Open Sans",Arial,sans-serif;color:var(--white)}
  .flyer{position:relative;width:1200px;height:800px;background:var(--white)}

  .hero-photo{position:absolute;left:0;top:0;width:1200px;height:366px;
    background:linear-gradient(180deg,#c9b2a8 0%,#e7dcd3 30%,#d8cfc8 55%,#b9a79a 75%,#5d5a58 100%)}
  .hero-ground{position:absolute;left:0;top:505px;width:1200px;height:19px;
    background:linear-gradient(90deg,#2f3137,#4a4c52 50%,#34363b)}

  .overlay{position:absolute;left:0;top:366px;width:1200px;height:139px;background:var(--brand-blue)}
  .overlay-title{position:absolute;left:200px;width:436px;top:3px;text-align:center;
    font-weight:300;font-size:68px;letter-spacing:1px}
  .overlay-subtitle{position:absolute;left:100px;width:600px;top:99px;text-align:center;
    font-style:italic;font-size:21px}
  .overlay-divider{position:absolute;left:860px;top:13px;width:1px;height:111px;background:var(--white)}
  .brand-mark{position:absolute;left:950px;top:48px;display:flex;align-items:center;gap:10px;
    font-weight:600;font-size:30px;letter-spacing:2px}
  .brand-mark .square{width:22px;height:22px;background:var(--white)}

  .address-bar{position:absolute;left:0;top:524px;width:1200px;height:37px;
    text-align:center;color:var(--ink-blue);font-weight:500;font-size:23px;line-height:37px;letter-spacing:.3px}

  .info-panel{position:absolute;left:0;top:561px;width:906px;height:187px;background:var(--brand-blue)}
  .side-photo{position:absolute;left:908px;top:561px;width:292px;height:187px;
    background:linear-gradient(180deg,#c7b7b0 0%,#e3d8cf 35%,#cdbfb3 60%,#5f5f63 100%)}
  .col-divider{position:absolute;top:11px;width:1px;height:166px;background:var(--white)}

  .agent-name{position:absolute;left:12px;top:11px;font-family:"Crimson Text",Georgia,serif;
    font-variant:small-caps;font-size:24px;line-height:1;border-bottom:1px solid var(--white)}
  .agent-title{position:absolute;left:12px;top:36px;font-size:14px}
  .agent-contact{position:absolute;left:8px;display:flex;align-items:center;gap:5px;font-size:13.5px;white-space:nowrap}
  .agent-contact.email{font-size:10px;letter-spacing:-.2px}
  .agent-contact svg{width:14px;height:14px;flex:none}
  .agent-photo{position:absolute;left:10px;top:684px;width:85px;height:111px;
    background:linear-gradient(180deg,#f0f0f0 0%,#d8d4d0 45%,#2a2a2e 100%)}

  .badge{position:absolute;background:var(--white)}
  .pitch-title{position:absolute;left:202px;width:261px;top:36px;text-align:center;font-weight:400;font-size:18px}
  .pitch-body{position:absolute;left:203px;width:259px;top:66px;text-align:center;font-size:12.2px;line-height:13.2px;white-space:nowrap}

  .services{position:absolute;left:463px;width:229px;top:76px;text-align:center;font-size:16px}
  .services-rule{position:absolute;left:538px;width:80px;top:107px;height:1px;background:rgba(255,255,255,.7)}
  .location{position:absolute;left:463px;width:229px;top:116px;text-align:center;font-weight:500;font-size:14px;line-height:17px}

  .features{position:absolute;left:712px;top:5px;list-style:none;font-size:16px;line-height:20px}
  .features li{position:relative;padding-left:25px}
  .features li svg{position:absolute;left:0;top:3px;width:14px;height:14px}

  .fine-print{position:absolute;left:0;width:1200px;top:770px;text-align:center;color:var(--ink);font-size:15.5px}
</style>
</head>
<body>
<main class="flyer">
  <div class="hero-photo" role="img" aria-label="Photo of the two-storey white commercial office building with dormers and parked cars at sunset"></div>
  <div class="hero-ground" role="img" aria-label="Asphalt parking lot continuing below the overlay"></div>

  <section class="overlay">
    <h1 class="overlay-title">FOR SALE</h1>
    <p class="overlay-subtitle">Potential Income Producing Commercial Office Building</p>
    <div class="overlay-divider"></div>
    <div class="brand-mark"><span class="square"></span>QTN HOMES</div>
  </section>

  <h2 class="address-bar">42 BRENTON DR., SCHAUMBURG, IL 60174 - ASKING PRICE: $650,000</h2>

  <section class="info-panel">
    <div class="agent-name">Dev Marlo</div>
    <div class="agent-title">Managing Broker</div>
    <div class="agent-contact" style="top:76px">
      <svg viewBox="0 0 16 16"><rect width="16" height="16" rx="3" fill="#111"/><path d="M4.5 3.5l2 2-1 1.3c.6 1.4 1.6 2.4 3 3l1.3-1 2 2-1.3 1.7C7 12 4 9 3 5z" fill="#fff"/></svg>
      847-555-0148
    </div>
    <div class="agent-contact email" style="top:99px">
      <svg viewBox="0 0 16 16"><rect width="16" height="16" rx="3" fill="#111"/><rect x="3" y="4.5" width="10" height="7" fill="none" stroke="#fff"/><path d="M3 4.5l5 4 5-4" fill="none" stroke="#fff"/></svg>
      dev.marlo@qtnhomes-example.com
    </div>

    <div class="col-divider" style="left:202px"></div>
    <div class="badge" style="left:262px;top:6px;width:54px;height:24px"></div>
    <div class="badge" style="left:375px;top:5px;width:26px;height:26px"></div>
    <h3 class="pitch-title">Looking to Buy or Sell?</h3>
    <p class="pitch-body">I’m your one-stop,<br>full service licensed real estate broker.<br>I deal with all types of real estate<br>properties: Homes, Condos, Townhomes,<br>Multi-Unit Apartment Buildings and<br>Commercial Spaces.<br>Let My Experience Guide You Through<br>Every Step of the Process!</p>

    <div class="col-divider" style="left:463px"></div>
    <div class="badge" style="left:514px;top:8px;width:136px;height:57px"></div>
    <p class="services">Residential &amp; Commercial</p>
    <div class="services-rule"></div>
    <p class="location">Located seconds away from the<br>Kettering Rd. &amp; Palden Rd.<br>Intersection</p>

    <div class="col-divider" style="left:692px"></div>
    <ul class="features">
      <li><svg viewBox="0 0 14 14"><circle cx="7" cy="7" r="6.2" fill="none" stroke="#fff" stroke-width="1.3"/><path d="M5.5 4l3.5 3-3.5 3z" fill="#fff"/></svg>Completely vacant</li>
      <li><svg viewBox="0 0 14 14"><circle cx="7" cy="7" r="6.2" fill="none" stroke="#fff" stroke-width="1.3"/><path d="M5.5 4l3.5 3-3.5 3z" fill="#fff"/></svg>10,000 sq. ft. building</li>
      <li><svg viewBox="0 0 14 14"><circle cx="7" cy="7" r="6.2" fill="none" stroke="#fff" stroke-width="1.3"/><path d="M5.5 4l3.5 3-3.5 3z" fill="#fff"/></svg>55 Car Parking</li>
      <li><svg viewBox="0 0 14 14"><circle cx="7" cy="7" r="6.2" fill="none" stroke="#fff" stroke-width="1.3"/><path d="M5.5 4l3.5 3-3.5 3z" fill="#fff"/></svg>1.38 acre lot</li>
      <li><svg viewBox="0 0 14 14"><circle cx="7" cy="7" r="6.2" fill="none" stroke="#fff" stroke-width="1.3"/><path d="M5.5 4l3.5 3-3.5 3z" fill="#fff"/></svg>Over 20 offices and<br>5 bathrooms.</li>
      <li><svg viewBox="0 0 14 14"><circle cx="7" cy="7" r="6.2" fill="none" stroke="#fff" stroke-width="1.3"/><path d="M5.5 4l3.5 3-3.5 3z" fill="#fff"/></svg>Lease out individual<br>office spaces for great<br>monthly cash flow</li>
    </ul>
  </section>

  <div class="side-photo" role="img" aria-label="Side view of the office building row with dormers and parking lot at dusk"></div>
  <div class="agent-photo" role="img" aria-label="Portrait of the managing broker in a dark suit"></div>

  <p class="fine-print">©2018 QTN Homes, Inc. All Rights Reserved</p>
</main>
</body>
</html>
```